Creating business cards for our new private medical clinic in London

Hey everyone,

We are starting a new private medical clinic in central London. We already have our logo (please see the 2 different layouts of the logo attached.) Please note that we are not restricted to using only this font in the card though.

The cards will be printed by "Pekko." The cards have a textured surface and a coloured middle layer - please see this webpage for the exact product spec (https://www.pekkoprint.example/uk/products/velvet/business-cards.html). We're overall looking for a modern yet highly professional look. We'd like the cards to have Square edges and NOT rounded please.

We need a standard card that uses one or both of our logo's colours (blue and green), and another card for premium customers, that uses black with either gold/silver/bronze. On the black coloured cads, please could you add the word "Black Account" or the word "Black" under the logo text - wherever you think it looks best?

_________________

AMENDMENT TO BRIEF:

1) The first batch of our cards are to be promotional cards and need to have more information. Could please have one card that is more like an "information card" that has the following information: - (There's a lot there and we might need to slim this down once we see the cards.)

GP appointments £70
-Feeling unwell
-Referrals to private specialists
-Sexual health check up
-Contraception
-Second opinion

Launch Offer
First appointment £40 with this card until 30 September 2017

Book online

2) Could you see whether we could add a 'strap line' to the card, something like: “Stay in Optimal Health”

_____________

The files attached have 2 versions of our logo - one linear and with the words 'stacked'; we think that the stacked logo may work better for the business card but we'd love to see different versions.

On one side of the card could we please see a coloured background, with a design containing our logo? On the other side of the card, please could we have a different coloured or white background and the information below.

Address: THE HARROWFIELD CLINIC @ FitVanta, 19 Bramblecote Lane, London, EC2Z 4QJ
Open: Mon-Fri (early & late appointments)
Book Online: www.harrowfieldclinic.example
Email: bookings@harrowfieldclinic.example
Phone number: (We don't have this yet - but please leave a space for this to go into.)

Other possible design features:

Because our clinic is located in the financial district of London, anything that represents this (e.g. The City of London's skyline - i.e. financial district - could look nice (example buildings include: The Pinecone, The Teacup-Tower, The Wedgehouse, St Aldric Minster, Keep of Brennmoor, Gantry Crossing, The Spindle). We wondered whether a outline or drawing of these buildings in the background of the card could look nice. Please see the image link below to get an idea of the skyline we're looking for:

https://img.stockvale.example/z/skyline-hand-drawn-city-pastel-shades-heritage-buildings-futuristic-81920457.jpg

The following image links are examples of cards that we've seen online and like the overall feel of (of course our colours are different):

http://www.craftnook.example/diverse/2/goodcards/73014589122.jpg
http://cardheron.example/wp-content/uploads/2013/01/cool-business-cards-saffron.jpg
https://cardfolio.example/wp-content/uploads/20461-cool-business-card-mockup.jpg
http://www.plinthworks.example/wp-content/uploads/edd/2015/08/Modern-Tutor-Business-Card-Template-Preview.jpg
http://lorvelandkit.example/wp-content/uploads/2017/01/design-a-business-card-cool-business-card-designsqx83.jpg
http://makerspindle.example/resources/files/articles/harbor-print/copper-foil-business-cards.jpg

STATIONARY:
We will also need the following stationary designed by our chosen designer. We’d like stationary to use one or both the colours of our logo (ie Green and Blue). Please use these colours to add any additional design features to stationary - other similar palette colours can also be used. Our logo font is - abeatbyKai - and this could be used in other parts of the stationary, but please feel free to try other fonts too. We prefer sans serif fonts.

Overall - we are open to all ideas but we need a look and feel that looks modern and highly professional. For our letter, prescription and medical report templates we need these to be PDFs and word processing files that can merge relevant data and text into different sections.

The information required on various pieces of stationary are as follows:

Letterheads:
These need to have:
Clinic's: Logo / Address / Phone Number / Website / Email address / Recipients address.
The letter can have address data either at the top or as a footer. We're happy to see designs that use either to see which one looks best (same goes for other pieces of stationary too.)

Invoices:
Invoice number: (Unique code for document)
Invoice Date:
Clinic’s: Logo / Address / Phone Number / Website / Email address
Services: Service Code / Name of Service / Price
Total Price:
PAYLO, Cardwise and Northern Remit Logos
Patient details: Patient’s Name / Address

Prescription Pads:
Prescription number: (Unique code for document)
Clinic details: Clinic’s Logo / Address / Phone Number / Website / Email address
Patient details needed include: Patient’s Name / Date of birth / address
Blank space required to write the name of medication
Doctors Signature: and space for signature
MPB Number: and space for this to be entered

Templates for our medical reports:
These are reports we will be printed (on good quality paper) for patients after they have had a complete health check. They will include a text summary, and the results of any tests (with graphs) and images of scans. Please could we see how text/titles/headings/tables etc could be styled?
They will need the following details: -
Clinic details needed include: Clinic’s Logo / Address / Phone Number / Website / Email address
Date of Report:
Then the following sections need to be includes:
1) Free Text Space
2) Space for images and text
3) Space for blood test and text

___________________

Thanks so much everyone.

All the best,

Tev and Dane

Target Market(s)

City of London
Private Healthcare

Industry/Entity Type

Health Care

Contact Information for Business Card

Font styles to use
Sans Serif

Colors
33a6d7
25a0d3
add136
9bcb3c
cadf82
85acd3
3276b5
0255a3
85cae6

Requirements
Must have
• Please see project description for details.
Nice to have
• Perhaps a outline/drawing/illustration of the City of London skyline (i.e. the Pinecone and surrounding buildings)

```html
<!DOCTYPE html>
<html lang="en">
<head>
<meta charset="utf-8">
<title>The Harrowfield Clinic – Business Cards</title>
<link href="https://fonts.googleapis.com/css2?family=Questrial&family=Open+Sans:wght@400;700&display=swap" rel="stylesheet">
<style>
  :root {
    --backdrop: #8a8a8a;
    --clinic-blue: #52b6de;
    --clinic-green: #add136;
    --card-black: #0a0a0a;
    --silver: #c4c6c8;
    --muted-grey: #b9b9b9;
    --white: #ffffff;
  }
  * { margin: 0; padding: 0; box-sizing: border-box; }
  html, body { width: 1200px; height: 900px; overflow: hidden; }
  body {
    background: linear-gradient(#7e7e7e, var(--backdrop) 60%, #939393);
    position: relative;
    font-family: "Open Sans", Arial, sans-serif;
  }
  .card {
    position: absolute;
    top: 306px;
    width: 439px;
    height: 271px;
    overflow: hidden;
  }
  .card--info { left: 149px; background: var(--clinic-blue); color: var(--white); }
  .card--brand { left: 609px; background: var(--card-black); }

  .feature-square {
    position: absolute;
    top: 10px;
    width: 250px;
    height: 250px;
    border: 14px solid var(--white);
    background: var(--clinic-blue);
  }
  .card--info .feature-square { left: 323px; }
  .card--brand .feature-square { left: -137px; }

  .wordmark { position: absolute; font-family: "Questrial", Arial, sans-serif; }
  .wordmark__name { display: block; white-space: nowrap; }
  .wordmark__tagline {
    display: block;
    font-family: "Open Sans", Arial, sans-serif;
    letter-spacing: 1px;
    text-transform: uppercase;
    text-align: right;
    white-space: nowrap;
  }
  .card--info .wordmark { left: 24px; top: 46px; color: var(--white); }
  .card--info .wordmark__name { font-size: 26px; line-height: 30px; }
  .card--info .wordmark__tagline { font-size: 7.5px; margin-top: 1px; }

  .card--brand .wordmark { right: 18px; top: 204px; color: var(--clinic-blue); }
  .card--brand .wordmark__name { font-size: 22px; line-height: 25px; }
  .card--brand .wordmark__tagline { font-size: 6px; color: var(--muted-grey); margin-top: 1px; }
  .wordmark__tier {
    display: block;
    margin-top: 4px;
    font-family: "Open Sans", Arial, sans-serif;
    font-size: 9px;
    font-weight: 700;
    letter-spacing: 3px;
    text-transform: uppercase;
    text-align: right;
    color: var(--silver);
  }
  .brand-mark {
    position: absolute;
    left: 255px; top: 108px;
    width: 82px; height: 82px;
    background: var(--clinic-green);
  }

  .contact { position: absolute; left: 24px; font-size: 12.5px; line-height: 16px; }
  .contact--address { top: 127px; }
  .contact--lines { top: 169px; list-style: none; }
  .contact--lines li { display: flex; align-items: center; gap: 6px; }
  .contact--lines svg { width: 10px; height: 10px; fill: var(--white); }
  .contact--hours { top: 210px; line-height: 20px; }
  .contact strong { font-weight: 700; }
</style>
</head>
<body>
  <section class="card card--info" aria-label="Business card, contact side">
    <div class="feature-square"></div>
    <div class="wordmark">
      <span class="wordmark__name">The Harrowfield Clinic</span>
      <span class="wordmark__tagline">Private General Practice</span>
    </div>
    <p class="contact contact--address">THE HARROWFIELD CLINIC @ FitVanta,<br>19 Bramblecote Lane, London, EC2Z 4QJ</p>
    <ul class="contact contact--lines">
      <li><svg viewBox="0 0 10 10" aria-hidden="true"><path d="M2 1h2l1 2-1.2 1a5 5 0 0 0 2.2 2.2L7 5l2 1v2a1 1 0 0 1-1 1A7 7 0 0 1 1 2a1 1 0 0 1 1-1z"/></svg>020 7946 0321</li>
      <li><svg viewBox="0 0 10 10" aria-hidden="true"><path d="M1 2h8v6H1z M1 2l4 3 4-3" stroke="#52b6de" stroke-width="0.8"/></svg>bookings@harrowfieldclinic.example</li>
    </ul>
    <p class="contact contact--hours"><strong>Open:</strong> Mon-Fri (early &amp; late appointments)<br><strong>Book Online:</strong> www.harrowfieldclinic.example</p>
  </section>

  <section class="card card--brand" aria-label="Business card, brand side">
    <div class="feature-square"></div>
    <div class="brand-mark"></div>
    <div class="wordmark">
      <span class="wordmark__name">The Harrowfield Clinic</span>
      <span class="wordmark__tagline">Private General Practice</span>
      <span class="wordmark__tier">Black</span>
    </div>
  </section>
</body>
</html>
```